Brightvale Crew Word Press Website

We need a graphical, fun website that conveys our messaging of providing the Best-In-Class Signature Marketing System for Mortgage Loan Officers and Realtors. Our system uses AI and Predictive Analysis to uncover the 'Gold' hidden in contact databases. The 'Gold' is defined as people who are in the market or likely to be in the market soon. We place that 'Gold' in the form of Contact Name, Address, Phone and Email on a Daily To Do List detailing what type of contact should be made.

Target Market(s)

Mortgage Loan Officers and Realtors

Industry/Entity Type

Mortgage & Real Estate

Coding

Coded - Design and coding required

Number of Pages Required

5+ page

Requirements
Must have
• I like the look of this site- https://www.homeloanpromostudio.example/
Nice to have
• Please create a flow that is similar to https://www.homeloanpromostudio.example/, but better, more dynamic. Site must be responsive and mobile friendly. Site will have embedded videos. Site need to convey a message of hope, imagination, innovation, results oriented, better than the rest, victory!
Should not have
• Nothing cheesy or low class.

```html
<!DOCTYPE html>
<html lang="en">
<head>
<meta charset="utf-8">
<title>Brightvale Crew — AI Lead Marketing for Loan Officers and Realtors</title>
<link href="https://fonts.googleapis.com/css2?family=Montserrat:wght@400;500;600;700&family=Lato:wght@400;700&display=swap" rel="stylesheet">
<style>
:root{
  --blue:#0f9bd7;
  --yellow:#ecc43c;
  --ink:#222;
  --text:#555;
  --soft:#eef4fb;
  --white:#fff;
  --black:#0b0b0b;
}
*{box-sizing:border-box;margin:0;padding:0}
html,body{width:1200px;height:4946px;overflow:hidden}
body{position:relative;font-family:"Lato",sans-serif;color:var(--text);background:var(--white)}
.abs{position:absolute}
h1,h2,h3,h4,.nav,.btn{font-family:"Montserrat",sans-serif}
.btn{position:absolute;display:flex;align-items:center;justify-content:center;gap:8px;background:var(--blue);color:#fff;border-radius:20px;font-size:13px;font-weight:500;white-space:nowrap}
p.copy{font-size:12.5px;line-height:21px;color:var(--text)}
p.copy+p.copy{margin-top:21px}

/* top bar */
.topbar{top:0;left:0;width:1200px;height:31px;background:var(--blue);color:#fff;font-size:12px}
.topbar .item{position:absolute;top:8px;display:flex;gap:6px;align-items:center}
.topbar .social{position:absolute;right:0;top:0;height:31px;width:270px;background:var(--yellow);clip-path:polygon(8% 0,100% 0,100% 100%,0 100%)}
.topbar .social span{position:absolute;top:8px;width:15px;height:15px;border-radius:3px;background:rgba(255,255,255,.85)}

/* header */
.header{top:31px;left:0;width:1200px;height:126px;background:#fff}
.brand{position:absolute;display:flex;align-items:center;gap:8px;font-family:"Montserrat",sans-serif;font-weight:700;color:var(--blue);text-transform:uppercase;letter-spacing:1px;white-space:nowrap}
.brand i{display:block;border-radius:50%;background:var(--yellow)}
.nav a{position:absolute;top:54px;font-size:15px;color:#333;text-decoration:none}
.nav a.active{color:var(--blue)}
.nav a.active:after{content:"";position:absolute;left:0;right:0;bottom:-10px;height:2px;background:var(--blue)}
.quote{left:966px;top:42px;width:157px;height:40px;background:linear-gradient(90deg,var(--blue) 72%,var(--yellow) 72%);font-size:12px}

/* hero */
.hero{top:157px;left:0;width:1200px;height:700px;overflow:hidden}
.hero-photo{position:absolute;inset:0;background:linear-gradient(100deg,#6a4a3a 0%,#b8826a 30%,#d96a3a 48%,#e9e4dc 70%,#cfc9bf 100%)}
.hero-photo:after{content:"";position:absolute;inset:0;background:linear-gradient(90deg,rgba(0,0,0,.5),rgba(0,0,0,0) 55%)}
.hero .kicker{left:132px;top:258px;color:#fff;font-size:13px}
.hero .headline{left:132px;top:280px;color:#fff;font-size:31px;line-height:41px;font-weight:600;text-transform:uppercase}
.hero .headline .row{display:flex;align-items:center;gap:12px}
.play{display:inline-flex;width:40px;height:40px;border-radius:50%;background:var(--blue)}
.watch{font-family:"Lato",sans-serif;font-size:13px;font-weight:400;text-transform:none}
.calc{left:739px;top:81px;width:359px;height:472px;background:rgba(236,196,60,.85)}
.calc .bar{height:62px;background:var(--blue);color:#fff;font-family:"Montserrat",sans-serif;font-weight:600;font-size:19px;display:flex;align-items:center;justify-content:center;text-transform:uppercase}
.calc label{position:absolute;left:42px;font-size:13px;color:#222}
.calc .field{position:absolute;left:40px;width:306px;height:42px;background:#fff;font-size:13px;color:#333;padding:13px 14px;display:flex;justify-content:space-between}
.calc .go{position:absolute;left:40px;top:418px;width:306px;height:44px;background:var(--blue);color:#fff;font-size:14px;display:flex;align-items:center;justify-content:center}

/* shared */
.sec-title{position:absolute;left:0;width:1200px;text-align:center;color:var(--ink);font-weight:600}
.art{position:absolute}

/* services */
.services{top:1498px;left:0;width:1200px;height:791px;background:var(--soft)}
.card{position:absolute;width:250px;height:257px;background:#fff;padding:30px 22px}
.card.hl{background:var(--yellow)}
.card svg.icon{width:64px;height:64px;stroke:var(--blue);fill:none;stroke-width:2}
.card.hl svg.icon{stroke:#333}
.card h4{font-size:13px;font-weight:600;color:var(--ink);margin:14px 0 8px;text-transform:uppercase;white-space:nowrap}
.card p{font-size:12px;line-height:15px;color:#444}
.card .arrow{position:absolute;left:22px;top:194px;width:48px;height:26px;background:var(--yellow);clip-path:polygon(0 0,100% 0,80% 100%,0 100%)}
.card.hl .arrow{background:var(--blue)}
.card .arrow:after{content:"";position:absolute;left:8px;top:12px;width:24px;height:2px;background:#222}
.card .arrow:before{content:"";position:absolute;left:26px;top:8px;width:7px;height:7px;border-top:2px solid #222;border-right:2px solid #222;transform:rotate(45deg)}
.card.hl .arrow:after{background:#fff}.card.hl .arrow:before{border-color:#fff}

/* forms */
.input{position:absolute;height:38px;border:1px solid #ddd;font-size:12px;color:#666;padding:11px 14px;display:flex;justify-content:space-between}

/* footer */
.footer{top:4512px;left:0;width:1200px;height:365px;background:var(--black);color:#fff}
.footer h4{position:absolute;top:123px;font-size:16px;font-weight:600;text-transform:uppercase}
.footer ul{position:absolute;list-style:none;font-size:13px;line-height:23px}
.footer ul li:before{content:"> "}
.copyright{top:4877px;left:0;width:1200px;height:69px;background:#fff;font-size:12px;color:#333}
.sc{position:absolute;top:20px;width:34px;height:34px;border-radius:50%;background:#111}
.sc.b{background:var(--blue)}
</style>
</head>
<body>

<!-- top bar -->
<div class="abs topbar">
  <div class="item" style="left:75px">
    <svg width="14" height="11" viewBox="0 0 14 11"><rect x="0.5" y="0.5" width="13" height="10" fill="none" stroke="#fff"/><path d="M1 1l6 5 6-5" fill="none" stroke="#fff"/></svg>
    +1 555 014 7722
  </div>
  <div class="item" style="left:527px">
    <svg width="12" height="12" viewBox="0 0 24 24"><path d="M6 2l4 5-2 3c1 3 3 5 6 6l3-2 5 4-3 4C10 22 2 14 2 5z" fill="#fff"/></svg>
    info@brightvalecrew.com
  </div>
  <div class="social">
    <span style="left:60px"></span><span style="left:102px"></span><span style="left:146px"></span><span style="left:190px"></span>
  </div>
</div>

<!-- header -->
<header class="abs header">
  <div class="brand" style="left:77px;top:48px;font-size:18px"><i style="width:26px;height:26px"></i>Brightvale Crew</div>
  <nav class="nav">
    <a class="active" style="left:512px">Home</a>
    <a style="left:599px">About</a>
    <a style="left:686px">Services</a>
    <a style="left:789px">Blog</a>
    <a style="left:865px">Contact</a>
  </nav>
  <div class="btn quote">Get A Demo <span>⟶</span></div>
</header>

<!-- hero -->
<section class="abs hero">
  <div class="hero-photo" role="img" aria-label="Smiling loan officer shaking hands with a client across a desk"></div>
  <div class="abs kicker">AI Marketing For Loan Officers &amp; Realtors</div>
  <h1 class="abs headline">
    <div>Find the gold in</div>
    <div class="row">your list <span class="play"><svg width="40" height="40"><path d="M17 14l9 6-9 6z" fill="#fff"/></svg></span><span class="watch">Watch Video</span></div>
  </h1>
  <div class="abs calc">
    <div class="bar">Find Your Hidden Gold</div>
    <label style="top:76px">Contacts In Database</label>
    <div class="field" style="top:102px"><span>4,000</span><span>⌄</span></div>
    <label style="top:157px">Your Role</label>
    <div class="field" style="top:181px"><span>Loan Officer</span><span>⌄</span></div>
    <label style="top:237px">Market Area</label>
    <div class="field" style="top:259px"><span>Statewide</span><span>⌄</span></div>
    <label style="top:314px">Daily To-Do List Size</label>
    <div class="field" style="top:338px"><span>15 Contacts</span><span>⌄</span></div>
    <div class="go">Calculate My Gold</div>
  </div>
  <svg class="abs" style="left:0;top:0" width="1200" height="700" viewBox="0 0 1200 700">
    <polygon points="0,582 620,650 1200,582 1200,670 620,700 0,670" fill="var(--yellow)"/>
    <polygon points="330,640 960,630 620,700" fill="var(--blue)"/>
    <polygon points="0,670 620,700 1200,670 1200,700 0,700" fill="#fff"/>
  </svg>
</section>

<!-- about -->
<section>
  <h2 class="sec-title" style="top:946px;font-size:31px">About Our Company</h2>
  <div class="sec-title" style="top:992px;font-size:9px;font-family:Montserrat,sans-serif">WHY SHOULD YOU CHOOSE US?</div>
  <div class="art" style="left:144px;top:1000px;width:432px;height:382px;border-radius:24px;background:radial-gradient(circle at 50% 45%,#dbeefa,#f4f8fc 70%,#fff)" role="img" aria-label="Illustration of analysts beside a large monitor with charts and a magnifier"></div>
  <div class="abs" style="left:626px;top:1046px;width:462px">
    <p class="copy">Brightvale Crew is the best-in-class signature marketing system built for mortgage loan officers and realtors who want real results, not more noise.</p>
    <p class="copy">Our AI and predictive analysis scan your contact database every day to uncover the gold: the people who are in the market now or likely to be in the market soon. No guessing, no cold lists, just clear signals you can act on today.</p>
    <p class="copy">Each morning that gold lands on your Daily To-Do List with name, address, phone and email, plus the type of contact to make, so you always know who to call next.</p>
  </div>
  <div class="btn" style="left:630px;top:1334px;width:153px;height:39px">Read More</div>
</section>

<!-- services -->
<section class="abs services">
  <h2 class="sec-title" style="top:68px;font-size:32px">OUR SERVICES</h2>
  <div class="card" style="left:73px;top:138px">
    <svg class="icon" viewBox="0 0 64 64"><circle cx="32" cy="32" r="18"/><circle cx="32" cy="32" r="9"/><path d="M32 6v10M32 48v10M6 32h10M48 32h10"/></svg>
    <h4>AI Lead Discovery</h4><p>Our AI scans your database daily to surface contacts about to move.</p><span class="arrow"></span></div>
  <div class="card hl" style="left:340px;top:138px">
    <svg class="icon" viewBox="0 0 64 64"><path d="M10 52h44M16 52V36M28 52V26M40 52V32M52 52V14M14 30l12-10 12 8 14-14"/></svg>
    <h4>Predictive Analysis</h4><p>Models score each contact so you know who is likely in the market soon.</p><span class="arrow"></span></div>
  <div class="card" style="left:607px;top:138px">
    <svg class="icon" viewBox="0 0 64 64"><rect x="14" y="10" width="36" height="46" rx="3"/><path d="M22 24l4 4 8-8M22 38l4 4 8-8M38 26h6M38 40h6"/></svg>
    <h4>Daily To-Do List</h4><p>Your gold delivered each morning with the right type of contact to make.</p><span class="arrow"></span></div>
  <div class="card" style="left:874px;top:138px">
    <svg class="icon" viewBox="0 0 64 64"><circle cx="24" cy="22" r="9"/><path d="M8 52c0-10 7-16 16-16s16 6 16 16M42 20h14M42 30h14M42 40h10"/></svg>
    <h4>Contact Enrichment</h4><p>Name, address, phone and email kept current and ready for outreach.</p><span class="arrow"></span></div>

  <div class="card" style="left:73px;top:414px">
    <svg class="icon" viewBox="0 0 64 64"><path d="M32 8a16 16 0 0 1 16 16v12l6 8H10l6-8V24A16 16 0 0 1 32 8zM26 50a6 6 0 0 0 12 0"/></svg>
    <h4>Refinance Alerts</h4><p>Instant alerts when past clients show signs of a refinance or a move.</p><span class="arrow"></span></div>
  <div class="card" style="left:340px;top:414px">
    <svg class="icon" viewBox="0 0 64 64"><rect x="18" y="8" width="22" height="44" rx="3"/><rect x="34" y="20" width="18" height="14"/><path d="M10 18h12v10H10z"/></svg>
    <h4>Social Media Growth</h4><p>Branded posts that keep you top of mind with your whole sphere.</p><span class="arrow"></span></div>
  <div class="card" style="left:607px;top:414px">
    <svg class="icon" viewBox="0 0 64 64"><path d="M10 14h44v28H30l-12 10V42h-8z"/><path d="M22 28h2M31 28h2M40 28h2"/></svg>
    <h4>Mortgage Chatbot</h4><p>A smart assistant that answers leads and books calls around the clock.</p><span class="arrow"></span></div>
  <div class="card" style="left:874px;top:414px">
    <svg class="icon" viewBox="0 0 64 64"><circle cx="28" cy="28" r="16"/><path d="M40 40l14 14M20 30l6-6 5 5 6-7"/></svg>
    <h4>SEO</h4><p>Local search pages that bring buyers and sellers straight to you.</p><span class="arrow"></span></div>
</section>

<!-- daily gold list -->
<section>
  <h2 class="abs" style="left:111px;top:2422px;font-size:32px;font-weight:600;color:var(--ink)">THE DAILY GOLD LIST</h2>
  <div class="abs" style="left:115px;top:2470px;width:470px">
    <p class="copy">Stop digging through spreadsheets. Brightvale Crew turns the contacts you already own into a short, focused list of people ready to talk.</p>
    <p class="copy">Every lead on the list comes with a clear next step: a call, a text, an email or a mailer. Predictive signals rank each contact so the hottest opportunities rise to the top and nothing slips through the cracks.</p>
    <p class="copy">Loan officers and realtors using the system spend less time hunting and more time closing, with a steady daily rhythm that builds a stronger pipeline.</p>
  </div>
  <div class="btn" style="left:115px;top:2757px;width:152px;height:37px">Read More</div>
  <div class="art" style="left:605px;top:2419px;width:575px;height:432px;background:radial-gradient(ellipse at 50% 45%,#f3d9a8,#e9eef7 55%,#fff 80%)" role="img" aria-label="Laptop and phone showing the daily to-do list dashboard with ranked contacts"></div>
</section>

<!-- strike gold -->
<section class="abs" style="top:2913px;left:0;width:1200px;height:629px">
  <div class="abs" style="inset:0;background:linear-gradient(110deg,#dcd5cc,#eeeae4 45%,#f4f1ec)" role="img" aria-label="House-shaped keychain with a key resting on a pale wooden surface"></div>
  <h2 class="abs" style="left:520px;width:604px;text-align:center;top:188px;font-size:32px;font-weight:600;color:var(--ink)">STRIKE GOLD EVERY DAY</h2>
  <div class="abs" style="left:802px;top:243px;width:40px;height:2px;background:var(--blue)"></div>
  <div class="abs" style="left:580px;top:270px;width:470px;text-align:center">
    <p class="copy">Imagine starting each morning knowing exactly which past clients and prospects are about to buy, sell or refinance.</p>
    <p class="copy">That is the Brightvale Crew promise: innovation that turns your database into closed loans and listings. Book a consultation and we will show you the gold hiding in your own contacts.</p>
  </div>
  <div class="btn" style="left:705px;top:451px;width:220px;height:35px;font-size:12px">SCHEDULE CONSULTATION</div>
</section>

<!-- request access -->
<section>
  <h2 class="sec-title" style="top:3662px;font-size:32px">START FINDING YOUR GOLD</h2>
  <div class="abs" style="left:464px;top:3729px;display:flex;align-items:center;gap:8px;font-size:12px;font-family:Montserrat,sans-serif;color:var(--ink)">
    <span style="width:15px;height:15px;border-radius:50%;background:var(--blue)"></span>REAL ESTATE AGENTS
    <span style="width:15px;height:15px;border-radius:50%;background:#ddd;margin-left:18px"></span>LOAN OFFICER
  </div>
  <div class="input" style="left:250px;top:3779px;width:222px">Name</div>
  <div class="input" style="left:486px;top:3779px;width:224px">Email</div>
  <div class="input" style="left:724px;top:3779px;width:224px"><span>License State</span><span>⌄</span></div>
  <div class="btn" style="left:488px;top:3854px;width:220px;height:38px">Request A Demo</div>
</section>

<!-- testimonials -->
<section>
  <div class="sec-title" style="top:3974px;font-size:12px;font-family:Montserrat,sans-serif">TESTIMONIALS</div>
  <h2 class="sec-title" style="top:4000px;font-size:32px">PEOPLE ARE SAYING ABOUT US</h2>
  <div class="abs" style="left:218px;top:4080px;width:50px;height:50px;border-radius:50%;background:#bfe3f6"></div>
  <div class="abs" style="left:185px;top:4076px;width:372px;height:372px;border-radius:50%;background:linear-gradient(160deg,#c9b79f,#7f8a93 60%,#4d5864)" role="img" aria-label="Family with a child on a parent's shoulders in front of a house"></div>
  <div class="abs" style="left:605px;top:4090px;width:68px;height:68px;border-radius:50%;background:var(--yellow);color:#222;font:700 34px/68px Montserrat,sans-serif;text-align:center">“</div>
  <div class="abs" style="left:689px;top:4108px;font:600 14px Montserrat,sans-serif;color:var(--ink)">Marisol Keene</div>
  <div class="abs" style="left:689px;top:4130px;font-size:13px;color:#555">Senior Loan Officer</div>
  <div class="abs" style="left:624px;top:4186px;width:462px">
    <p class="copy">Within the first month my Daily To-Do List pointed me to six past clients ready to refinance. I had no idea they were even looking.</p>
    <p class="copy">I used to spend hours guessing who to call. Now I open the list, follow the suggested contact type and get straight to work. My pipeline has never been this full or this predictable.</p>
  </div>
  <div class="abs" style="left:624px;top:4352px;color:var(--yellow);font-size:20px;letter-spacing:6px">★★★★★</div>
  <div class="abs" style="left:624px;top:4406px;display:flex;gap:12px">
    <span style="width:13px;height:13px;border-radius:50%;background:var(--blue)"></span>
    <span style="width:13px;height:13px;border-radius:50%;background:#ddd"></span>
    <span style="width:13px;height:13px;border-radius:50%;background:#ddd"></span>
  </div>
</section>

<!-- footer -->
<footer class="abs footer">
  <div class="brand" style="left:73px;top:160px;font-size:20px;color:var(--yellow)"><i style="width:32px;height:32px;background:var(--blue)"></i>Brightvale Crew</div>
  <h4 style="left:388px">Quick Links</h4>
  <ul style="left:390px;top:168px"><li>Home</li><li>About</li><li>Services</li><li>Blog</li><li>Contact us</li></ul>
  <h4 style="left:609px">Contact Detail</h4>
  <div class="abs" style="left:609px;top:170px;font-size:14px;line-height:22px">
    <div>☏ &nbsp;+1 555 014 7722</div>
    <div style="margin-top:10px">✉ &nbsp;info@brightvalecrew.com</div>
    <div style="margin-top:10px">⌖ &nbsp;48 Larkspur Row<br>&nbsp;&nbsp;&nbsp;&nbsp;#210, Fenwick, OR 97000</div>
  </div>
  <h4 style="left:876px">Newsletter</h4>
  <div class="abs" style="left:876px;top:170px;font-size:13px">Weekly tips to grow your pipeline</div>
  <div class="abs" style="left:876px;top:194px;width:245px;height:33px;background:#fff;border-radius:17px;color:#777;font-size:12px;font-style:italic;padding:9px 20px">Email Address</div>
  <div class="btn" style="left:876px;top:238px;width:245px;height:31px;font-size:12px">SUBSCRIBE</div>
</footer>
<div class="abs copyright">
  <div class="abs" style="left:79px;top:28px">Copyright © 2022 <b>BRIGHTVALE CREW</b>. All Rights Reserved.</div>
  <span class="sc b" style="left:945px"></span><span class="sc" style="left:993px"></span><span class="sc" style="left:1041px"></span><span class="sc" style="left:1087px"></span>
</div>

</body>
</html>
```